Calder Wynd Company Profile

We have all the written content for our company profile and just need the background graphics and layout designed, this can be seen at our website www.calder-wynd.example or in the attached company profiles
We are happy with the content as far as wording and our logo are concerned, we are looking to revamp the background and layout.
The intention is for this to be printed as a brochure where the inside of the rear page has a pocket at the bottom so that our relevant affiliated companies brochures can be inserted into to complete the package depending on who we are presenting it to.

Target Market(s)

Oil & Gas, Power Generation, Mining, Maritime, Marine, Automation, Engineering

Industry/Entity Type

Engineering Consulting

Colors

Designer to choose colors to be used in the design.

Requirements
Must have
• Existing provided content
Nice to have
• engineering background and images that pop
Should not have
• our target market is Oil & Gas, Power Generation, Mining, Maritime, Marine, Automation, Engineering so it should not have content that does not relate to these industries

```html
<!DOCTYPE html>
<html lang="en">
<head>
<meta charset="utf-8">
<title>Calder Wynd – Company Profile Cover</title>
<link rel="stylesheet" href="https://fonts.googleapis.com/css2?family=Exo+2:wght@300;400;800&family=Open+Sans:wght@400;600&display=swap">
<style>
  :root {
    --charcoal: #4a4a4a;
    --charcoal-deep: #3c3c3c;
    --orange: #f0a023;
    --paper: #f2f2f2;
    --ink: #2e2e2e;
    --sky-top: #c9d2da;
    --sky-mid: #eef1f3;
    --plant: #9aa0a6;
    --stage: #e6e7ec;
  }
  * { margin: 0; padding: 0; box-sizing: border-box; }
  html, body { width: 1200px; height: 902px; overflow: hidden; background: var(--stage); }
  .spread {
    position: absolute; left: 63px; top: 71px;
    width: 1074px; height: 760px;
    display: flex;
    box-shadow: 0 6px 24px rgba(0,0,0,.18);
  }
  .page { position: relative; width: 537px; height: 760px; overflow: hidden; }
  .page svg.shapes { position: absolute; inset: 0; width: 100%; height: 100%; }
  .photo {
    position: absolute; inset: 0;
    background: linear-gradient(180deg, var(--sky-top) 0%, var(--sky-mid) 45%, #d7dade 62%, var(--plant) 82%, #7f868c 100%);
  }
  /* Back cover */
  .contact {
    position: absolute; left: 34px; top: 588px; width: 330px;
    font-family: "Open Sans", sans-serif; color: var(--ink);
  }
  .brand {
    display: flex; align-items: center; gap: 10px;
    font-family: "Exo 2", sans-serif; font-weight: 800;
    font-size: 26px; line-height: 1; letter-spacing: .5px;
    color: var(--charcoal); text-transform: uppercase;
  }
  .brand-dot { width: 18px; height: 18px; border-radius: 50%; background: var(--orange); flex: none; }
  .contact ul { list-style: none; margin-top: 12px; font-size: 10.5px; line-height: 1.45; }
  .contact li { display: flex; align-items: flex-start; gap: 10px; margin-bottom: 2px; }
  .contact li svg { width: 11px; height: 11px; margin-top: 2px; flex: none; }
  .contact li.phone { font-weight: 600; font-size: 15px; line-height: 1.2; margin-bottom: 6px; }
  .contact li.phone svg { margin-top: 3px; }
  /* Front cover */
  .front .brand { position: absolute; left: 78px; top: 74px; font-size: 24px; }
  .title { position: absolute; left: 88px; top: 132px; font-family: "Exo 2", sans-serif; }
  .title .lead {
    font-weight: 800; font-size: 27px; line-height: 1.02;
    color: var(--orange); text-transform: uppercase; letter-spacing: .5px;
  }
  .title .sub {
    font-weight: 300; font-size: 31px; line-height: 1.05;
    color: var(--ink); margin-top: 6px;
  }
  .title .sub span { display: block; padding-left: 18px; }
  .badge {
    position: absolute; left: 378px; top: 255px; width: 128px; height: 128px;
    border-radius: 50%; background: var(--orange);
    border: 4px solid #fff; box-shadow: 0 0 0 2px var(--charcoal-deep);
    display: flex; flex-direction: column; align-items: center; justify-content: center;
    font-family: "Exo 2", sans-serif; color: var(--charcoal-deep); text-transform: uppercase;
    transform: rotate(-12deg);
  }
  .badge .small { font-size: 14px; font-weight: 400; }
  .badge .big { font-size: 21px; font-weight: 400; }
  .url-band {
    position: absolute; left: 0; bottom: 0; width: 100%; height: 42px;
    background: var(--charcoal);
    font-family: "Open Sans", sans-serif; font-size: 12px; letter-spacing: 4px;
    color: #e0e0e0; text-transform: uppercase;
    display: flex; align-items: center; padding-left: 90px;
  }
</style>
</head>
<body>
<main class="spread">

  <section class="page back">
    <div class="photo" role="img" aria-label="Photograph of an oil refinery with tall chimneys under a cloudy sky"></div>
    <svg class="shapes" viewBox="0 0 537 760" aria-hidden="true">
      <polygon fill="var(--orange)" points="0,0 198,0 243,95 218,100 328,300 298,305 428,740 0,740"/>
      <polygon fill="var(--charcoal)" points="0,0 170,0 215,95 190,100 300,300 270,305 400,740 0,740"/>
      <polygon fill="var(--paper)" points="0,565 348,565 398,740 0,740"/>
      <rect fill="var(--charcoal)" x="0" y="740" width="537" height="20"/>
    </svg>
    <div class="contact">
      <div class="brand"><span class="brand-dot"></span>Calder Wynd</div>
      <ul>
        <li class="phone"><svg viewBox="0 0 12 12"><path fill="#2e2e2e" d="M2 1h2.5l1 3-1.5 1a7 7 0 0 0 3 3l1-1.5 3 1V10a1 1 0 0 1-1 1A9 9 0 0 1 1 2a1 1 0 0 1 1-1z"/></svg>+44-1632-960-418</li>
        <li><svg viewBox="0 0 12 12"><path d="M1 3h10v6H1z M1 3l5 3.5L11 3" fill="none" stroke="#2e2e2e" stroke-width="1.2"/></svg>consultants@calder-wynd.example</li>
        <li><svg viewBox="0 0 12 12"><circle cx="6" cy="6" r="5" fill="none" stroke="#2e2e2e" stroke-width="1.2"/><path d="M1 6h10M6 1c-2.5 3-2.5 7 0 10M6 1c2.5 3 2.5 7 0 10" fill="none" stroke="#2e2e2e" stroke-width="1"/></svg>www.calder-wynd.example</li>
        <li><svg viewBox="0 0 12 12"><path fill="#2e2e2e" d="M6 1 11 6H9.5v5h-2.5V8H5v3H2.5V6H1z"/></svg><span>Suite 4B, 9th Floor,<br>Harbour Point 12 Quay Street, Northport</span></li>
      </ul>
    </div>
  </section>

  <section class="page front">
    <div class="photo" role="img" aria-label="Photograph of an industrial plant with process towers and pipework against a cloudy sky"></div>
    <svg class="shapes" viewBox="0 0 537 760" aria-hidden="true">
      <polygon fill="var(--orange)" points="285,0 537,0 537,718 430,470 455,462 385,325 410,317 340,165 368,157"/>
      <polygon fill="var(--charcoal)" points="325,0 537,0 537,650 470,465 495,457 425,325 450,317 380,165 408,157"/>
    </svg>
    <div class="brand"><span class="brand-dot"></span>Calder Wynd</div>
    <div class="title">
      <p class="lead">Technical<br>Manpower</p>
      <p class="sub">&amp; consultancy<span>services</span></p>
    </div>
    <div class="badge"><span class="small">Company</span><span class="big">Profile</span></div>
    <div class="url-band">www.calder-wynd.example</div>
  </section>

</main>
</body>
</html>
```